Creative/innovative law firm website

A law firm website that immediately looks different from other law firm websites. We like the color scheme (dark background with warm, neutral colors) and simple, organic logos (trees, leaves, etc.) of this website: https://nimbleway.law/

We'll be offering creative/innovative solutions to complex problems faced by state governments, industries, other law firms, and individuals. We're located in Montana (U.S.A.), and the outdoors is a huge part of our lives and identities.

We will need a home page, an "About Us" page with a separate subpage for each attorney (two attorneys), a blog or "Publications" page, a payment portal (which will integrate with Quindle), and a "Services" page.

```html
<!DOCTYPE html>
<html lang="en">
<head>
<meta charset="utf-8">
<title>Harrow &amp; Pine P.C</title>
<link rel="stylesheet" href="https://fonts.googleapis.com/css2?family=Playfair+Display:ital,wght@0,400;0,600;1,400&family=Lato:wght@400;700&display=swap">
<style>
:root{
  --gold:#b8740a;
  --ink:#0b0b0b;
  --slate:#262626;
  --white:#ffffff;
}
*{margin:0;padding:0;box-sizing:border-box}
html,body{width:1200px;height:4601px;overflow:hidden}
body{position:relative;background:var(--ink);color:var(--white);font-family:'Lato',sans-serif}
.abs{position:absolute}
.serif{font-family:'Playfair Display',serif}
.btn{position:absolute;display:flex;align-items:center;justify-content:center;font-size:14px;color:var(--white);background:var(--gold);font-family:'Lato',sans-serif}
.btn.dark{background:#111}
.photo{position:absolute}

.hero{position:absolute;left:0;top:0;width:1200px;height:634px;background:linear-gradient(90deg,#0f1418 0%,#1c232a 45%,#12171b 100%)}
.brand{left:71px;top:28px;display:flex;align-items:center;gap:12px;font-size:16px;letter-spacing:.3px}
.brand-mark{width:40px;height:40px;border-radius:50%;border:2px solid var(--gold)}
.nav{top:24px;left:592px;display:flex;gap:42px;font-size:13px}
.contact-top{left:993px;top:22px;font-family:'Playfair Display',serif;font-size:14px;line-height:22px}
.contact-top span{color:var(--gold)}
.hero-title{left:761px;top:232px;font-size:46px;line-height:58px;font-weight:400}
.hero-title i{font-size:40px}
.hero-title .accent{color:var(--gold);font-style:italic}
.dots{display:flex;gap:16px}
.dots b{width:9px;height:9px;border-radius:50%;background:#777;display:block}
.dots b.on{background:var(--gold)}

.about{position:absolute;left:0;top:634px;width:1200px;height:714px;background:linear-gradient(90deg,#0c0c0c,#241e19 60%,#0c0c0c)}
.about h2{font-size:38px;font-weight:400}
.about p{font-size:14px;line-height:26px}

.section-title{position:absolute;width:1200px;text-align:center;font-size:34px;font-weight:400}
.card{position:absolute;width:250px;height:257px;overflow:hidden}
.card h3{position:absolute;left:30px;top:95px;font-size:17px;line-height:24px;font-weight:400}

.name{font-size:30px;line-height:34px}
.role{font-size:16px;line-height:22px}

.pub h3{font-size:19px;font-weight:400;margin-top:28px}
.pub p{font-size:14px;line-height:26px;margin-top:12px}
.date{position:absolute;width:79px;height:71px;background:var(--gold);font-family:'Playfair Display',serif;font-size:21px;line-height:24px;text-align:center;padding-top:11px}

.award{position:absolute;width:250px;height:191px;background:#2c2c2c;text-align:center;clip-path:polygon(0 0,200px 0,250px 45px,250px 191px,0 191px)}
.award h4{position:absolute;left:0;top:98px;width:250px;font-family:'Playfair Display',serif;font-weight:600;font-size:18px;line-height:24px}
.award p{position:absolute;left:0;top:130px;width:250px;font-size:14px;line-height:24px}

.field{position:absolute;left:125px;width:345px;background:#fff;color:#222;font-size:12px;padding:10px 12px}
</style>
</head>
<body>

<section class="hero">
  <div class="photo" role="img" aria-label="Two smiling attorneys in suits standing together" style="left:110px;top:60px;width:490px;height:574px;background:linear-gradient(90deg,#5d6166 0%,#74787d 30%,#4a4e55 52%,#1f2a44 70%,#27324d 100%)"></div>
  <div class="abs brand"><span class="brand-mark"></span>HARROW &amp; PINE P.C</div>
  <nav class="abs nav"><span>Home</span><span>About</span><span>Services</span><span>Publications</span></nav>
  <div class="abs contact-top">Free Contact<br><span>(1) 555-0142-210</span></div>
  <h1 class="abs hero-title serif"><i>We’re Ready</i><br>For A <span class="accent">Fight</span><br>Against Injustice</h1>
  <div class="btn" style="left:761px;top:440px;width:187px;height:37px">Consultation Request</div>
  <div class="abs dots" style="left:1071px;top:578px"><b></b><b class="on"></b><b></b></div>
</section>

<section class="about">
  <div class="photo" role="img" aria-label="Law library with tall shelves of books" style="left:500px;top:41px;width:629px;height:250px;background:linear-gradient(90deg,#2a211a,#5a4634 40%,#3b2e23 70%,#6a5440)"></div>
  <div class="abs" style="left:105px;top:89px;width:425px;height:581px;border:1px solid var(--gold)"></div>
  <div class="photo" role="img" aria-label="Two people shaking hands beside a gavel" style="left:71px;top:112px;width:465px;height:536px;background:linear-gradient(135deg,#a6a6a6,#6a6a6a 45%,#3a3a3a)"></div>
  <div class="photo" role="img" aria-label="Law books with a gavel in front" style="left:309px;top:191px;width:253px;height:380px;background:linear-gradient(180deg,#6b5642,#3d3126);border:2px solid #777"></div>
  <svg class="abs" style="left:387px;top:246px" width="813" height="424"><polygon points="175,0 813,0 813,424 0,424" fill="var(--gold)"/></svg>
  <div class="abs" style="left:589px;top:298px;width:545px">
    <h2 class="serif">About Us</h2>
    <p style="margin-top:14px">Many desktop publishing packages and web page editors now use Lorem Ipsum as their default model text,and a search for ‘lorem ipsum’ will uncover many web sites still in their infancy. Various versions have evolved over the years, sometimes by accident,</p>
    <p style="margin-top:12px">There are many variations of passages of Lorem Ipsum available, but the majority have suffered alteration in some form, by injected humour, or randomised words which don’t look even slightly believable.</p>
  </div>
  <div class="btn dark" style="left:589px;top:568px;width:111px;height:39px">Read More</div>
</section>

<h2 class="section-title serif" style="top:1441px">Solution We Offer</h2>
<div class="card" style="left:71px;top:1520px">
  <div class="photo" role="img" aria-label="State capitol columns" style="inset:0;background:linear-gradient(135deg,#7a7a7a,#3a3a3a)"></div>
  <svg class="abs" style="left:0;top:0" width="250" height="257"><polygon points="0,257 250,140 250,257" fill="#000"/><line x1="52" y1="238" x2="210" y2="163" stroke="var(--gold)" stroke-width="2"/><g fill="var(--gold)"><rect x="32" y="70" width="36" height="6"/><rect x="36" y="56" width="4" height="14"/><rect x="46" y="56" width="4" height="14"/><rect x="56" y="56" width="4" height="14"/><polygon points="30,56 50,40 70,56"/></g></svg>
  <h3 class="serif">Problems Faced By<br>State Governments</h3>
</div>
<div class="card" style="left:341px;top:1520px">
  <div class="photo" role="img" aria-label="Industrial skyline" style="inset:0;background:linear-gradient(135deg,#6a6a6a,#333)"></div>
  <svg class="abs" style="left:0;top:0" width="250" height="257"><polygon points="0,257 250,140 250,257" fill="#000"/><line x1="52" y1="238" x2="210" y2="163" stroke="var(--gold)" stroke-width="2"/><g fill="var(--gold)"><rect x="32" y="48" width="6" height="28"/><polygon points="32,76 32,60 44,54 44,62 56,54 56,62 68,54 68,76"/></g></svg>
  <h3 class="serif">Problems Faced By<br>Industries</h3>
</div>
<div class="card" style="left:611px;top:1520px">
  <div class="photo" role="img" aria-label="Law books and scales" style="inset:0;background:linear-gradient(135deg,#6c6c6c,#343434)"></div>
  <svg class="abs" style="left:0;top:0" width="250" height="257"><polygon points="0,257 250,140 250,257" fill="#000"/><line x1="52" y1="238" x2="210" y2="163" stroke="var(--gold)" stroke-width="2"/><g stroke="var(--gold)" stroke-width="3" fill="none"><line x1="50" y1="44" x2="50" y2="76"/><line x1="34" y1="50" x2="66" y2="50"/><path d="M30 64 L34 50 L38 64 Z M62 64 L66 50 L70 64 Z"/><line x1="40" y1="76" x2="60" y2="76"/></g></svg>
  <h3 class="serif">Problems Faced By<br>Other law Firms</h3>
</div>
<div class="card" style="left:880px;top:1520px">
  <div class="photo" role="img" aria-label="Chess pieces on a board" style="inset:0;background:linear-gradient(135deg,#7e7e7e,#383838)"></div>
  <svg class="abs" style="left:0;top:0" width="250" height="257"><polygon points="0,257 250,140 250,257" fill="#000"/><line x1="52" y1="238" x2="210" y2="163" stroke="var(--gold)" stroke-width="2"/><g fill="var(--gold)"><rect x="40" y="44" width="20" height="10" transform="rotate(-35 50 49)"/><rect x="48" y="52" width="5" height="20" transform="rotate(-35 50 62)"/><rect x="30" y="72" width="34" height="6"/></g></svg>
  <h3 class="serif">Problems Faced By<br>Individuals</h3>
</div>
<div class="btn" style="left:543px;top:1841px;width:114px;height:40px">View More</div>

<section class="abs" style="left:0;top:1959px;width:1200px;height:523px;background:linear-gradient(90deg,#3a3a3a,#151515 30%,#151515 70%,#3a3a3a)">
  <div class="photo" role="img" aria-label="Senior partner in a grey suit with arms crossed" style="left:110px;top:20px;width:320px;height:503px;background:linear-gradient(90deg,#5a5a5a,#7c7c7c 45%,#555)"></div>
  <div class="photo" role="img" aria-label="Junior partner in a navy suit" style="left:750px;top:20px;width:330px;height:503px;background:linear-gradient(90deg,#1d2740,#2e3a5a 50%,#1a2236)"></div>
  <div class="abs serif" style="left:300px;top:22px;width:239px;text-align:right"><div class="name">Dell Marsh</div></div>
  <div class="abs" style="left:300px;top:56px;width:239px;text-align:right"><div class="role">LLB TEP<br>Senior Partner</div></div>
  <div class="abs" style="left:553px;top:28px;width:4px;height:46px;background:var(--gold)"></div>
  <div class="abs" style="left:643px;top:28px;width:4px;height:46px;background:var(--gold)"></div>
  <div class="abs serif" style="left:661px;top:22px"><div class="name">Owen Reyd</div></div>
  <div class="abs" style="left:661px;top:56px"><div class="role">LLB TEP<br>Junior Partner</div></div>
  <svg class="abs" style="left:316px;top:148px" width="582" height="313"><polygon points="163,0 413,0 582,313 0,313" fill="var(--gold)"/></svg>
  <div class="abs serif" style="left:450px;top:238px;width:300px;text-align:center;font-size:34px;line-height:46px">Meet Our<br>Attorneys</div>
  <div class="btn dark" style="left:543px;top:345px;width:112px;height:39px">View Details</div>
</section>

<h2 class="section-title serif" style="top:2550px">Publications</h2>
<div class="abs pub" style="left:71px;top:2631px;width:340px">
  <div class="photo" role="img" aria-label="Lawyer at a laptop with gavel and documents" style="position:relative;width:313px;height:176px;background:linear-gradient(135deg,#e2ddd5,#a88a68 60%,#6a4a30)"></div>
  <div class="date" style="left:259px;top:50px">JUN<br>27</div>
  <h3 class="serif">Lorem Ipsum</h3>
  <p>Many desktop publishing packages and web page editors now use Lorem Ipsum as their default model text .</p>
</div>
<div class="btn" style="left:71px;top:2961px;width:113px;height:39px">Read More</div>
<div class="abs pub" style="left:430px;top:2631px;width:340px">
  <div class="photo" role="img" aria-label="Hands holding golden scales of justice" style="position:relative;width:313px;height:176px;background:linear-gradient(135deg,#2c2c2c,#7a6334)"></div>
  <div class="date" style="left:259px;top:50px">JUl<br>17</div>
  <h3 class="serif">Lorem Ipsum</h3>
  <p>Many desktop publishing packages and web page editors now use Lorem Ipsum as their default model text .</p>
</div>
<div class="btn" style="left:430px;top:2961px;width:113px;height:39px">Read More</div>
<div class="abs pub" style="left:789px;top:2631px;width:340px">
  <div class="photo" role="img" aria-label="Statue of justice beside a gavel and book" style="position:relative;width:313px;height:176px;background:linear-gradient(135deg,#7c8a96,#4a3c30)"></div>
  <div class="date" style="left:259px;top:50px">SEP<br>27</div>
  <h3 class="serif">Lorem Ipsum</h3>
  <p>Many desktop publishing packages and web page editors now use Lorem Ipsum as their default model text .</p>
</div>
<div class="btn" style="left:789px;top:2961px;width:113px;height:39px">Read More</div>

<section class="abs" style="left:0;top:3090px;width:1200px;height:575px;background:var(--slate)">
  <svg class="abs" style="left:0;top:0" width="1200" height="575"><polygon points="0,0 291,0 291,209 0,480" fill="#1a1a1a"/><polygon points="291,209 1200,209 1200,575 0,575 0,480" fill="#232323"/></svg>
  <div class="photo" role="img" aria-label="Courthouse facade with columns in black and white" style="left:291px;top:66px;width:909px;height:143px;background:linear-gradient(90deg,#3e3e3e,#7a7a7a 45%,#9a9a9a 60%,#505050)"></div>
  <h2 class="abs serif" style="left:291px;top:114px;width:620px;text-align:center;font-size:34px;font-weight:400">Awards &amp; Membership</h2>
</section>
<div class="award" style="left:71px;top:3397px"><span class="abs" style="left:103px;top:36px;width:44px;height:44px;border-radius:50%;background:var(--gold)"></span><h4>Lorem Ipsum Dollar</h4><p>Many desktop publishing<br>packages .</p></div>
<div class="award" style="left:341px;top:3397px"><span class="abs" style="left:99px;top:32px;width:52px;height:52px;border-radius:50%;border:3px solid #fff"></span><h4>Lorem Ipsum Dollar</h4><p>Many desktop publishing<br>packages .</p></div>
<div class="award" style="left:611px;top:3397px"><span class="abs" style="left:101px;top:34px;width:48px;height:48px;border-radius:50%;background:var(--gold)"></span><h4>Lorem Ipsum Dollar</h4><p>Many desktop publishing<br>packages .</p></div>
<div class="award" style="left:879px;top:3397px"><span class="abs" style="left:101px;top:34px;width:48px;height:48px;border:3px solid #fff"></span><h4>Lorem Ipsum Dollar</h4><p>Many desktop publishing<br>packages .</p></div>
<div class="abs dots" style="left:571px;top:3620px;gap:14px"><b style="background:#fff"></b><b class="on"></b><b style="background:#fff"></b></div>

<section class="abs" style="left:0;top:3665px;width:1200px;height:664px;background:#141414">
  <div class="photo" role="img" aria-label="Dim city skyline with capitol dome" style="left:0;top:58px;width:1200px;height:606px;background:linear-gradient(180deg,#303030,#242424 50%,#141414)"></div>
</section>
<svg class="abs" style="left:71px;top:3768px" width="450" height="507"><polygon points="0,0 350,0 450,107 450,507 0,507" fill="var(--gold)"/></svg>
<h2 class="abs serif" style="left:123px;top:3848px;font-size:33px;font-weight:400">Don’t Hesitate To Ask</h2>
<div class="field" style="top:3907px;height:45px;padding-top:15px">Name :</div>
<div class="field" style="top:3959px;height:45px;padding-top:15px">Email :</div>
<div class="field" style="top:4009px;height:45px;padding-top:15px">Phone:</div>
<div class="field" style="top:4064px;height:77px;padding-top:16px">Choose A Subject :</div>
<div class="btn dark" style="left:125px;top:4152px;width:113px;height:39px">Submit</div>
<div class="abs serif" style="left:560px;top:3968px;width:500px;text-align:center;font-size:29px;line-height:52px;font-style:italic">Are you having any problems but<br>can’t consult to anyone?</div>
<div class="abs serif" style="left:560px;top:4080px;width:500px;text-align:center;font-size:37px;line-height:54px">Call Now !<br>(1) 555-0142-210</div>

<footer class="abs" style="left:0;top:4329px;width:1200px;height:272px;background:linear-gradient(180deg,#0e0e0e,#1a1a1a)">
  <div class="abs" style="left:520px;top:52px;display:flex;gap:9px"><span style="width:32px;height:32px;border-radius:50%;background:var(--gold)"></span><span style="width:32px;height:32px;border-radius:50%;background:var(--gold)"></span><span style="width:32px;height:32px;border-radius:50%;background:var(--gold)"></span><span style="width:32px;height:32px;border-radius:50%;background:var(--gold)"></span></div>
  <div class="abs" style="left:436px;top:96px;width:328px;height:61px;border:1px solid #fff;display:flex;align-items:center;justify-content:center;font-family:'Playfair Display',serif;font-size:19px">hello@harrowpine.net</div>
  <div class="abs" style="left:0;top:176px;width:1200px;text-align:center;font-size:15px">Alder Consulting 412 W. Larch Way, Bozeman Ridge, MT 59700</div>
  <div class="abs" style="left:0;top:217px;width:1200px;text-align:center;font-size:15px">© Copyright &nbsp;harrow &amp; pine 2021</div>
</footer>

</body>
</html>
```